Bag Design For Outdoors Industry

We are a Midwest seed company that is looking for a bag design for our Food Plot Product Line, "Ridgehorn". We are looking for a broad design that will work for several SKUs. Attached is the dieline for 4.5"x9.5"x20.75" bag and specifications for the print company. Also included are the brand standards and our catalog. The bag design should pull the themes and concepts established in the catalog. We will be placing 4"x9" labels on the front and back of the bag (design should have a guide for labels). Front of package will include a clear window to see the product. Use the attached layout PDF for a rough idea of how it should be formatted. The final design should convey the simple brand and overall themes.

Target Market(s)

Outdoor enthusiasts

Industry/Entity Type

Outdoors

Requirements
Must have
• Follow our provided branding, clear window

```html
<!DOCTYPE html>
<html lang="en">
<head>
<meta charset="utf-8">
<title>Ridgehorn Food Plot Seed – Bag Panels</title>
<link href="https://fonts.googleapis.com/css2?family=Oswald:wght@400;500;600&display=swap" rel="stylesheet">
<style>
  :root {
    --page: #ffffff;
    --sage: #dfe2c6;
    --sage-deep: #cfd3ad;
    --lime: #b7d24a;
    --lime-bright: #9cc83a;
    --leaf: #5aa832;
    --orange: #e08c1e;
    --orange-deep: #c97412;
    --ink: #353633;
    --label: #ffffff;
    --gold: #a88c5a;
    --window: #4a4b48;
  }
  * { margin: 0; padding: 0; box-sizing: border-box; }
  html, body { width: 1200px; height: 800px; overflow: hidden; background: var(--page); }
  body { position: relative; font-family: "Oswald", sans-serif; color: var(--ink); }

  .panel { position: absolute; overflow: hidden; }
  .panel-art {
    position: absolute; inset: 0;
    background:
      radial-gradient(circle at 80% 70%, var(--lime) 0 22%, transparent 23%),
      radial-gradient(ellipse at 15% 20%, var(--lime-bright) 0 20%, transparent 21%),
      radial-gradient(ellipse at 70% 15%, var(--leaf) 0 10%, transparent 11%),
      radial-gradient(ellipse at 10% 60%, var(--sage-deep) 0 18%, transparent 19%),
      linear-gradient(160deg, var(--sage) 0%, var(--sage-deep) 100%);
  }
  .seal-band { position: absolute; left: 0; right: 0; top: 0; height: 44px; background: linear-gradient(180deg, var(--lime-bright), var(--lime)); opacity: .85; }

  .front { left: 130px; top: 100px; width: 340px; height: 600px; }
  .back  { left: 720px; top: 120px; width: 340px; height: 560px; }
  .gusset { position: absolute; background: linear-gradient(90deg, var(--orange-deep), var(--orange) 45%, var(--orange-deep)); display: flex; align-items: center; justify-content: center; }
  .gusset-front { left: 470px; top: 100px; width: 90px; height: 600px; }
  .gusset-back  { left: 640px; top: 120px; width: 80px; height: 560px; }
  .gusset-name { writing-mode: vertical-rl; font-weight: 600; font-size: 40px; letter-spacing: 2px; color: var(--ink); }
  .gusset-sub { writing-mode: vertical-rl; font-size: 11px; letter-spacing: 2px; color: var(--ink); margin-left: 4px; font-weight: 400; }

  .brand { position: absolute; left: 0; right: 0; text-align: center; font-weight: 600; color: var(--ink); display: flex; align-items: center; justify-content: center; gap: 8px; }
  .brand-dot { width: 14px; height: 14px; border-radius: 50%; background: var(--ink); }
  .front .brand { top: 120px; font-size: 36px; }
  .back .brand { top: 300px; font-size: 22px; }
  .back .brand .brand-dot { width: 10px; height: 10px; }
  .brand-mark { position: absolute; left: 0; right: 0; text-align: center; font-weight: 600; color: var(--ink); }
  .front .brand-mark { top: 345px; font-size: 44px; }
  .back .brand-mark { top: 190px; font-size: 40px; }

  .label { position: absolute; background: var(--label); left: 30px; right: 30px; }
  .front .label { top: 190px; height: 150px; padding: 12px 22px; text-align: center; }
  .back .label { top: 360px; height: 140px; display: flex; align-items: center; justify-content: center; font-size: 15px; font-weight: 500; }

  .badges { display: flex; justify-content: center; gap: 4px; }
  .badge { background: var(--gold); color: var(--ink); font-size: 8px; font-weight: 500; padding: 2px 10px; }
  .label-title { font-size: 20px; font-weight: 500; margin-top: 8px; letter-spacing: .5px; }
  .wave { display: block; margin: 2px auto 0; }
  .label-tagline { font-size: 7px; font-weight: 500; margin-top: 8px; color: var(--ink); }
  .label-foot { display: flex; justify-content: space-between; align-items: flex-end; margin-top: 14px; text-align: left; }
  .fine { font-size: 5.5px; line-height: 1.3; width: 110px; }
  .net { font-size: 8px; font-weight: 500; margin-top: 3px; }
  .coverage { display: flex; align-items: center; gap: 4px; font-size: 9px; line-height: 1; }
  .coverage-badge { background: var(--gold); color: #fff; font-size: 14px; padding: 3px 5px; }

  .window { position: absolute; left: 0; bottom: 0; }
</style>
</head>
<body>

  <section class="panel front">
    <div class="panel-art" role="img" aria-label="Leaf line drawings over sage and lime blob shapes"></div>
    <div class="seal-band"></div>
    <div class="brand"><span class="brand-dot"></span>Ridgehorn</div>
    <div class="label">
      <div class="badges"><span class="badge">100%</span><span class="badge">ORGANIC &amp; NATURAL</span></div>
      <div class="label-title">PRIME FIELD PLOTS</div>
      <svg class="wave" width="40" height="6" viewBox="0 0 40 6"><path d="M0 3 Q2.5 0 5 3 T10 3 T15 3 T20 3 T25 3 T30 3 T35 3 T40 3" fill="none" stroke="#353633" stroke-width="1"/></svg>
      <div class="label-tagline">YOUR PATH TO STRONGER HERDS AND FULLER HUNTING SEASONS</div>
      <div class="label-foot">
        <div>
          <div class="fine">COATED SEED: PACKAGE HOLDS UP TO 30% COATING.</div>
          <div class="net">NET WT. 3 LB (1.36 KG)</div>
        </div>
        <div class="coverage"><span>COVERS<br>UP TO</span><span class="coverage-badge">1/2 ACRE</span></div>
      </div>
    </div>
    <div class="brand-mark">Ridgehorn</div>
    <svg class="window" width="340" height="600" viewBox="0 0 340 600" role="img" aria-label="Clear window showing seed inside">
      <polygon points="30,440 30,590 315,590" fill="var(--window)"/>
    </svg>
  </section>
  <div class="gusset gusset-front"><span class="gusset-name">RIDGEHORN</span><span class="gusset-sub">FOOD PLOT SEED</span></div>

  <div class="gusset gusset-back"><span class="gusset-name">RIDGEHORN</span><span class="gusset-sub">FOOD PLOT SEED</span></div>
  <section class="panel back">
    <div class="panel-art" role="img" aria-label="Leaf line drawings over sage and lime blob shapes"></div>
    <div class="seal-band"></div>
    <div class="brand-mark">Ridgehorn</div>
    <div class="brand"><span class="brand-dot"></span>Ridgehorn</div>
    <div class="label">PRODUCT INFORMATION LABEL</div>
  </section>

</body>
</html>
```